DJMarvelo.com

A clean-looking fun website.

MAP*

top* Video. (To host party footage and also to host live streams as they happen.

Tabs - Events, Livestream, Mixes, Playlists, Sign up, Photos, Bio, Shop

Links to Instagram, Facebook and Twitter, YouTube & Twitch

sign up sheet to take contact details for future promo.

References
http://www.djbrisklofton.com/
http://www.samharrowby.com/
https://bigredvolley.com/
https://www.djpravinofficial.com/
https://dunmoss.com/
https://www.ivanpelmo.com/bed/

I hope this helps.

```html
<!DOCTYPE html>
<html lang="en">
<head>
<meta charset="utf-8">
<title>DJ Marvelo</title>
<link href="https://fonts.googleapis.com/css2?family=Rubik:wght@500;700;900&family=Montserrat:wght@400;500;600&display=swap" rel="stylesheet">
<style>
:root{
  --pink:#d6145f;
  --black:#000;
  --ink:#0b0b0b;
  --panel:#161616;
  --gallery:#1b1b1b;
  --white:#fff;
  --muted:#c9c9c9;
  --line:#3a3a3a;
  --head:"Rubik",sans-serif;
  --body:"Montserrat",sans-serif;
}
*{margin:0;padding:0;box-sizing:border-box}
html,body{width:1200px;height:4084px;overflow:hidden;background:var(--black);color:var(--white);font-family:var(--body)}
.abs{position:absolute}
.section{position:absolute;left:0;width:1200px;overflow:hidden}
.kicker{font-family:var(--body);font-weight:400;font-size:19px;color:var(--white)}
.title{font-family:var(--head);font-weight:700;font-size:40px;letter-spacing:1px;text-transform:uppercase;line-height:1}
.btn{position:absolute;background:var(--pink);color:var(--white);font:600 13px var(--body);text-transform:uppercase;display:flex;align-items:center;justify-content:center;letter-spacing:.5px}
.photo{position:absolute}
.arrows{position:absolute;display:flex;gap:14px}
.play{position:absolute;border-radius:50%;background:var(--pink);display:flex;align-items:center;justify-content:center}
.play.white{background:var(--white)}

/* hero */
.hero{top:0;height:697px;background:linear-gradient(100deg,#0d0d0d 0%,#1f1f1f 45%,#3a3a3a 70%,#1a1a1a 100%)}
.hero-photo{left:520px;top:110px;width:680px;height:507px;background:radial-gradient(ellipse at 55% 35%,#6a6a6a 0%,#3a3a3a 40%,#161616 80%)}
.hero-deck{left:0;top:470px;width:700px;height:227px;background:linear-gradient(180deg,rgba(60,60,60,.0),#2a2a2a 60%,#1c1c1c)}
.nav{left:227px;top:0;width:748px;height:92px;display:flex;align-items:center}
.logo{font:700 34px var(--head);color:var(--white);letter-spacing:.5px}
.menu{margin-left:auto;display:flex;gap:19px;align-items:center;font:500 12px var(--body);text-transform:uppercase}
.menu .signup{background:var(--pink);padding:8px 14px;font-weight:600}
.frame{left:472px;top:160px;width:574px;height:380px;border:5px solid var(--pink)}
.hero-sub{left:225px;top:258px;font:400 50px var(--body)}
.hero-name{left:220px;top:316px;font:700 86px var(--head);line-height:1}
.social{left:90px;top:328px;width:14px}
.social .rule{width:2px;height:79px;background:var(--white);margin-left:6px}
.social .dot{width:9px;height:9px;background:var(--white);border-radius:50%;margin:14px 0 0 3px}
.social .dot:first-of-type{margin-top:22px}
.services{left:409px;top:617px;height:80px;display:flex}
.service{height:80px;background:#1a1a1a;display:flex;align-items:center;gap:12px;padding:0 22px 0 40px;font:600 13px var(--body);text-transform:uppercase;position:relative}
.service:nth-child(2){background:#151515}
.service:nth-child(3){background:#111}
.service .num{position:absolute;left:18px;top:8px;font:900 56px var(--head);color:#2a2a2a}
.service svg{position:relative}
.service span{position:relative}

/* bio */
.bio{top:697px;height:528px;background:var(--black)}
.bio-frame{left:227px;top:64px;width:340px;height:358px;border:4px solid #2b2b2b}
.bio-photo{left:260px;top:96px;width:341px;height:358px;background:linear-gradient(135deg,#6b4b8f 0%,#8a3a5c 45%,#3e3140 100%)}
.bio-kicker{left:547px;top:133px}
.bio-title{left:545px;top:167px}
.bio-text{left:648px;top:232px;width:330px;font:400 12.5px/19px var(--body);color:#e6e6e6}
.bio .btn{left:648px;top:371px;width:125px;height:35px}

/* mixes */
.mixes{top:1225px;height:476px;background:var(--panel)}
.mixes .kicker{left:227px;top:74px}
.mixes .title{left:224px;top:108px}
.mixes .arrows{left:922px;top:122px}
.mix{top:171px;width:183px;height:230px}
.mix-label{position:absolute;bottom:14px;left:0;width:100%;text-align:center;font:600 15px var(--body)}

/* events */
.events{top:1701px;height:653px;background:radial-gradient(ellipse at 50% 60%,#1e1418 0%,#0c0c0c 70%)}
.center{width:1200px;text-align:center;left:0}
.events .kicker.center{top:64px}
.events .title.center{top:96px}
.event{top:180px;width:240px}
.event .day{position:absolute;left:0;top:0;font:700 30px var(--head);color:var(--pink)}
.event .month{position:absolute;left:52px;top:3px;font:500 9px var(--body);text-transform:uppercase}
.event h3{position:absolute;left:52px;top:19px;font:700 20px/21px var(--head);width:190px}
.event p{position:absolute;left:52px;top:75px;width:180px;font:400 11.5px/17px var(--body);color:#d4d4d4}
.events .btn{left:539px;top:336px;width:124px;height:34px}
.events .divider{left:227px;top:425px;width:748px;height:1px;background:var(--line)}
.stream-word{left:0;top:432px;width:1200px;text-align:center;font:900 104px var(--head);color:#232323;letter-spacing:4px;line-height:1}

/* playlist */
.playlist{top:2354px;height:556px;background:var(--pink);overflow:visible}
.video{left:331px;top:2203px;width:538px;height:301px;background:linear-gradient(160deg,#b8a07a 0%,#6c5a4a 45%,#2c2624 100%)}
.playlist .kicker.center{top:190px}
.playlist .title.center{top:226px}
.track{left:266px;width:669px;height:50px;background:var(--white);display:flex;align-items:center}
.track .no{width:51px;height:50px;background:#111;display:flex;align-items:center;justify-content:center;font:700 22px var(--head)}
.track .info{margin-left:20px;width:340px}
.track .info b{display:block;font:700 18px/18px var(--head);color:var(--pink)}
.track .info small{font:400 11px var(--body);color:#444}
.track .vol{display:flex;align-items:center;gap:8px;width:120px}
.track .bar{width:48px;height:2px;background:var(--pink)}
.track .time{font:400 11px var(--body);color:#555;width:70px;margin-left:10px}
.track .end{margin-left:auto;width:68px;height:50px;border-left:1px solid #e4e4e4;display:flex;align-items:center;justify-content:center}

/* testimonials */
.feedback{top:2910px;height:365px;background:radial-gradient(ellipse at 50% 40%,#242424 0%,#0e0e0e 75%)}
.feedback .kicker.center{top:64px}
.feedback .title.center{top:98px}
.avatar{left:575px;top:155px;width:48px;height:48px;border-radius:50%;background:linear-gradient(#cfd6e0,#7d8898);border:2px solid var(--white)}
.quote{left:330px;top:224px;width:540px;text-align:center;font:400 12.5px/19px var(--body)}
.author{left:0;top:288px;width:1200px;text-align:center;font:600 12.5px var(--body)}
.feedback .arrow-l{left:230px;top:227px}
.feedback .arrow-r{left:952px;top:227px}

/* gallery */
.gallery{top:3275px;height:593px;background:var(--gallery)}
.gallery .kicker{left:227px;top:68px}
.gallery .title{left:224px;top:102px}
.gallery .arrows{left:922px;top:116px}
.shot{top:169px;width:176px;height:172px}
.gallery .btn{left:539px;top:372px;width:124px;height:34px}

/* newsletter + footer */
.news{left:227px;top:3780px;width:748px;height:88px;background:var(--pink);z-index:2}
.news small{position:absolute;left:29px;top:26px;font:500 10px var(--body);text-transform:uppercase}
.news h4{position:absolute;left:29px;top:41px;font:700 24px var(--head);text-transform:uppercase}
.news .field{position:absolute;left:377px;top:30px;width:245px;height:28px;border-bottom:1px solid var(--white);font:400 11px var(--body);padding-top:8px}
.news .sub{position:absolute;left:618px;top:24px;width:100px;height:30px;background:var(--white);color:var(--pink);font:600 12px var(--body);display:flex;align-items:center;justify-content:center;text-transform:uppercase}
.footer{top:3868px;height:216px;background:var(--ink)}
.footer .vline{top:0;width:1px;height:216px;background:#2a2a2a}
.footer .logo{position:absolute;left:230px;top:50px;font-size:44px}
.copy{left:227px;top:146px;font:400 11px/18px var(--body)}
.footer h5{position:absolute;top:53px;font:500 14px var(--body);text-transform:uppercase}
.links{top:85px;font:400 11px/18px var(--body)}
.links li{list-style:none}
.links li::before{content:"» ";}
.contact{left:796px;font:400 10.5px/15px var(--body)}
</style>
</head>
<body>

<header class="section hero">
  <div class="photo hero-photo" role="img" aria-label="DJ singing into a microphone over his decks, black and white"></div>
  <div class="photo hero-deck" role="img" aria-label="Mixing console in the foreground"></div>
  <div class="frame abs"></div>
  <nav class="nav abs">
    <div class="logo">Marvelo</div>
    <div class="menu">
      <span>Events</span><span>Livestream</span><span>Mixes</span><span>Playlists</span><span>Photos</span><span>Bio</span><span>Shop</span><span class="signup">Sign up</span>
    </div>
  </nav>
  <div class="abs hero-sub">Super Mix</div>
  <h1 class="abs hero-name">DJ Marvelo</h1>
  <div class="play" style="left:646px;top:302px;width:64px;height:64px"><svg width="22" height="24" viewBox="0 0 22 24"><path d="M2 1 21 12 2 23Z" fill="#fff"/></svg></div>
  <div class="abs social" aria-label="Social links">
    <div class="rule"></div>
    <div class="dot" title="Facebook"></div><div class="dot" title="Twitter"></div><div class="dot" title="Instagram"></div><div class="dot" title="LinkedIn"></div><div class="dot" title="YouTube"></div>
  </div>
  <div class="abs services">
    <div class="service"><span class="num">1</span>
      <svg width="36" height="34" viewBox="0 0 36 34" fill="none" stroke="#d6145f" stroke-width="2"><path d="M18 31C5 21 2 15 2 10a8 8 0 0 1 16-2 8 8 0 0 1 16 2c0 5-3 11-16 21Z"/><path d="M12 12c2-3 6-3 6 0"/></svg>
      <span>Weddings</span></div>
    <div class="service"><span class="num">2</span>
      <svg width="32" height="36" viewBox="0 0 32 36" fill="none" stroke="#d6145f" stroke-width="2"><path d="M4 6h24L16 20Z"/><path d="M16 20v12M9 33h14"/><circle cx="24" cy="5" r="4"/></svg>
      <span>Clubs &amp; Bars</span></div>
    <div class="service"><span class="num">3</span>
      <svg width="38" height="36" viewBox="0 0 38 36" fill="none" stroke="#d6145f" stroke-width="2"><circle cx="19" cy="18" r="5"/><circle cx="6" cy="6" r="3"/><circle cx="32" cy="6" r="3"/><circle cx="6" cy="30" r="3"/><circle cx="32" cy="30" r="3"/><path d="M8 8l7 6M30 8l-7 6M8 28l7-6M30 28l-7-6"/></svg>
      <span>Corporate Events</span></div>
  </div>
</header>

<section class="section bio">
  <div class="abs bio-frame"></div>
  <div class="photo bio-photo" role="img" aria-label="Smiling DJ with headphones behind the decks at a party"></div>
  <div class="abs kicker bio-kicker">Welcome To</div>
  <h2 class="abs title bio-title">My Biography</h2>
  <p class="abs bio-text">Lorem Ipsum is simply dummy text of the printing and typesetting industry. Lorem Ipsum has been at the industry's standard dummy text ever since the 1500s, when an unknown printer took a galley of type &amp; scrambled it to make a type specimen book. It has survived not only five centuries.</p>
  <div class="btn">Read More</div>
</section>

<section class="section mixes">
  <div class="abs kicker">DJ's Sets</div>
  <h2 class="abs title">Recent Mixes</h2>
  <div class="arrows"><svg width="22" height="14" viewBox="0 0 22 14" fill="none" stroke="#fff" stroke-width="1.6"><path d="M21 7H2M8 1 2 7l6 6"/></svg><svg width="22" height="14" viewBox="0 0 22 14" fill="none" stroke="#fff" stroke-width="1.6"><path d="M1 7h19M14 1l6 6-6 6"/></svg></div>
  <div class="photo mix" style="left:227px;background:linear-gradient(160deg,#e8b8cf,#b46b8c 50%,#3a2a30)" role="img" aria-label="Dancers on a pink lit floor behind a turntable"></div>
  <div class="photo mix" style="left:423px;background:linear-gradient(170deg,#2c4fb0,#1c2a66 55%,#0c0f22)" role="img" aria-label="DJ at a console under blue stage lights"></div>
  <div class="photo mix" style="left:621px;background:linear-gradient(175deg,#3a84e0,#16408f 55%,#0a1530)" role="img" aria-label="Wedding hall stage with blue lighting">
    <div class="play" style="left:68px;top:90px;width:46px;height:46px"><svg width="14" height="16" viewBox="0 0 14 16"><path d="M1 1 13 8 1 15Z" fill="#fff"/></svg></div>
    <div class="mix-label">Wedding Hall</div>
  </div>
  <div class="photo mix" style="left:819px;background:linear-gradient(160deg,#e0a24a,#7a4a1e 50%,#1a120c)" role="img" aria-label="Close-up of hands on a DJ controller"></div>
  <div class="photo mix" style="left:1016px;background:linear-gradient(150deg,#3b6cc7,#2a2f70 50%,#12122e)" role="img" aria-label="Female DJ with raised hand under blue light"></div>
</section>

<section class="section events">
  <div class="abs kicker center">Our Events</div>
  <h2 class="abs title center">Upcoming Dates</h2>
  <div class="abs event" style="left:224px"><span class="day">05</span><span class="month">August, 2021</span><h3>The Event Name Here!</h3><p>Lorem ipsum dolor sit amet, at consectetur adipiscing elit, sed do eiusmod tempor.</p></div>
  <div class="abs event" style="left:485px"><span class="day">18</span><span class="month">September, 2021</span><h3>The Event Name Here!</h3><p>Lorem ipsum dolor sit amet, at consectetur adipiscing elit, sed do eiusmod tempor.</p></div>
  <div class="abs event" style="left:747px"><span class="day">29</span><span class="month">September, 2021</span><h3>The Event Name Here!</h3><p>Lorem ipsum dolor sit amet, at consectetur adipiscing elit, sed do eiusmod tempor.</p></div>
  <div class="btn">View All</div>
  <div class="abs divider"></div>
  <div class="abs stream-word">LIVESTREAM</div>
</section>

<section class="section playlist">
  <div class="abs kicker center">Our Playlist</div>
  <h2 class="abs title center">Recent DJ's Sets</h2>
  <div class="abs track" style="top:299px"><div class="no">01</div><div class="info"><b>Recent Dj Playlist 1</b><small>Lorem Ipsum is simply dummy text.</small></div><div class="vol"><svg width="14" height="12" viewBox="0 0 14 12"><path d="M1 4h3l4-3v10L4 8H1Z" fill="#222"/><path d="M10 3q2 3 0 6" stroke="#222" fill="none"/></svg><div class="bar"></div></div><div class="time">000.55</div><div class="end"><div class="play" style="position:static;width:28px;height:28px"><svg width="10" height="12" viewBox="0 0 10 12"><path d="M1 1 9 6 1 11Z" fill="#fff"/></svg></div></div></div>
  <div class="abs track" style="top:363px"><div class="no">02</div><div class="info"><b>Recent Dj Playlist 2</b><small>Lorem Ipsum is simply dummy text.</small></div><div class="vol"><svg width="14" height="12" viewBox="0 0 14 12"><path d="M1 4h3l4-3v10L4 8H1Z" fill="#222"/><path d="M10 3q2 3 0 6" stroke="#222" fill="none"/></svg><div class="bar"></div></div><div class="time">000.55</div><div class="end"><div class="play" style="position:static;width:28px;height:28px"><svg width="10" height="12" viewBox="0 0 10 12"><path d="M1 1 9 6 1 11Z" fill="#fff"/></svg></div></div></div>
  <div class="abs track" style="top:425px"><div class="no">03</div><div class="info"><b>Recent Dj Playlist 3</b><small>Lorem Ipsum is simply dummy text.</small></div><div class="vol"><svg width="14" height="12" viewBox="0 0 14 12"><path d="M1 4h3l4-3v10L4 8H1Z" fill="#222"/><path d="M10 3q2 3 0 6" stroke="#222" fill="none"/></svg><div class="bar"></div></div><div class="time">000.55</div><div class="end"><div class="play" style="position:static;width:28px;height:28px"><svg width="10" height="12" viewBox="0 0 10 12"><path d="M1 1 9 6 1 11Z" fill="#fff"/></svg></div></div></div>
</section>

<div class="photo video" role="img" aria-label="Livestream video: blurred dance floor behind a DJ mixer"></div>
<div class="play white" style="left:576px;top:2331px;width:46px;height:46px"><svg width="14" height="16" viewBox="0 0 14 16"><path d="M1 1 13 8 1 15Z" fill="#d6145f"/></svg></div>

<section class="section feedback">
  <div class="abs kicker center">Testimonials</div>
  <h2 class="abs title center">Clubbers Feedback</h2>
  <div class="abs avatar" role="img" aria-label="Portrait of the reviewer"></div>
  <p class="abs quote">Lorem ipsum dolor sit amet, consectetur adipiscing elit, sed do eiusmod tempor incididunt labore et dolore magna aliqua. Ut enim ad minim veniam, quis nostrud exercitation ullam laboris nisi ut aliquip ex ea commodo consequat</p>
  <div class="abs author">- Daniel Reeves</div>
  <svg class="abs arrow-l" width="16" height="12" viewBox="0 0 16 12" fill="none" stroke="#fff" stroke-width="1.5"><path d="M15 6H2M6 1 1 6l5 5"/></svg>
  <svg class="abs arrow-r" width="16" height="12" viewBox="0 0 16 12" fill="none" stroke="#fff" stroke-width="1.5"><path d="M1 6h13M10 1l5 5-5 5"/></svg>
</section>

<section class="section gallery">
  <div class="abs kicker">DJ's Gallery</div>
  <h2 class="abs title">Latest Photos</h2>
  <div class="arrows"><svg width="22" height="14" viewBox="0 0 22 14" fill="none" stroke="#fff" stroke-width="1.6"><path d="M21 7H2M8 1 2 7l6 6"/></svg><svg width="22" height="14" viewBox="0 0 22 14" fill="none" stroke="#fff" stroke-width="1.6"><path d="M1 7h19M14 1l6 6-6 6"/></svg></div>
  <div class="photo shot" style="left:227px;background:linear-gradient(150deg,#2a4fa0,#7a3a70 50%,#1c1a2a)" role="img" aria-label="Hands scratching a record on a turntable"></div>
  <div class="photo shot" style="left:417px;background:linear-gradient(170deg,#c58ae6,#8a3cc0 50%,#3a1a50)" role="img" aria-label="Banquet hall lit in purple"></div>
  <div class="photo shot" style="left:609px;background:linear-gradient(170deg,#c8a58a,#6a4a3e 55%,#1e1714)" role="img" aria-label="Mixer in front of a blurred dance floor"></div>
  <div class="photo shot" style="left:799px;background:linear-gradient(160deg,#3c5a8c,#26324a 50%,#111)" role="img" aria-label="DJ working at a laptop and controller"></div>
  <div class="btn">View All</div>
</section>

<div class="abs news">
  <small>Upcoming events and special offers</small>
  <h4>Get Weekly Newsletters</h4>
  <div class="field">Your Email Address</div>
  <div class="sub">Subscribe</div>
</div>

<footer class="section footer">
  <div class="abs vline" style="left:476px"></div>
  <div class="abs vline" style="left:745px"></div>
  <div class="logo">Marvelo</div>
  <p class="abs copy">Copyrights © 2021 DJ Marvelo. All Rights<br>Are Reserved &nbsp;|&nbsp; Privacy Policy.</p>
  <h5 style="left:526px">Quick Links</h5>
  <ul class="abs links" style="left:526px"><li>Home</li><li>Bio</li><li>Events</li><li>Livestream</li><li>Playlists</li></ul>
  <ul class="abs links" style="left:634px"><li>Mixes</li><li>Sign up</li><li>Photos</li><li>Shop</li><li>Contact</li></ul>
  <h5 style="left:796px">Contact Us</h5>
  <svg class="abs" style="left:796px;top:90px" width="14" height="18" viewBox="0 0 14 18" fill="none" stroke="#fff" stroke-width="1.3"><path d="M7 17S1 10 1 6.5a6 6 0 0 1 12 0C13 10 7 17 7 17Z"/><circle cx="7" cy="6.5" r="2"/></svg>
  <p class="abs contact" style="left:826px;top:86px">DJ Marvelo<br>123 Sample Street, New City,<br>New State, NV 89117</p>
  <svg class="abs" style="left:796px;top:145px" width="18" height="13" viewBox="0 0 18 13" fill="none" stroke="#fff" stroke-width="1.3"><rect x="1" y="1" width="16" height="11"/><path d="M1 1l8 6 8-6"/></svg>
  <p class="abs contact" style="left:826px;top:139px">info@example.com<br>founder@example.com</p>
</footer>

</body>
</html>
```